Verdell Chiropractic, achieve your health goals, get better each day one step at a time

A mobile friendly site, fresh look, easy to navigate, has interface with pw/chirply, etc. Blog posts. Uses new logo. Content and address to current site is mirvaton.com. The current site will give you scope of project for content. The logo is not the final but close. Will upload final next week.
Convey the concept that heath is a process, it does not just happen. We take steps to achieve what we want in life including health.

Target Market(s)

30 to 70 year old. Needing health care

Industry/Entity Type

Health Care

Coding

Coded - Design and coding required

Number of Pages Required

5+ page

Font styles to use
Sans Serif

Colors

Designer to choose colors to be used in the design.

Requirements
Must have
• mobile friendly, easy to navigate, PW/Chirply interface, blog, room for current content
Nice to have
• potential for commerce, statistics
Should not have
• Same old look and feel as everything else out there

```html
<!DOCTYPE html>
<html lang="en">
<head>
<meta charset="utf-8">
<title>Verdell Chiropractic</title>
<link href="https://fonts.googleapis.com/css2?family=Oswald:wght@400;500;600&family=Open+Sans:wght@400;600;700&family=Lora:ital@1&display=swap" rel="stylesheet">
<style>
:root{
  --blue:#1b82d4;
  --blue-dark:#125e9c;
  --navy:#1d2a38;
  --green:#6cc04a;
  --ink:#3b3f45;
  --muted:#8a9099;
  --line:#e3e6ea;
  --paper:#ffffff;
  --footer:#1c1f24;
  --footer-deep:#15171b;
  --map:#e6e8ea;
}
*{box-sizing:border-box;margin:0;padding:0}
html,body{width:1200px;height:2860px;overflow:hidden;background:var(--paper)}
body{font-family:"Open Sans",Arial,sans-serif;color:var(--ink);position:relative}

/* hero */
.hero{position:absolute;left:0;top:0;width:1200px;height:528px;
  background:radial-gradient(ellipse at 62% 20%,#c4483a 0%,#a95e55 12%,#8f7d78 26%,#5e5f62 48%,#2f3237 80%,#1f2226 100%)}
.topbar{position:absolute;top:0;left:0;width:1200px;height:94px}
.brand{position:absolute;left:28px;top:10px;width:230px;height:72px;background:rgba(255,255,255,.94);
  display:flex;align-items:center;gap:10px;padding:0 14px}
.brand-dot{width:16px;height:16px;border-radius:50%;background:var(--blue)}
.brand-name{font-family:"Oswald",sans-serif;font-weight:500;font-size:21px;color:var(--blue-dark);letter-spacing:.5px}
.social{position:absolute;right:24px;top:10px;display:flex;gap:12px}
.social span{width:12px;height:12px;border-radius:50%;background:#fff;opacity:.8}
.nav{position:absolute;right:0;top:36px;height:48px;background:var(--navy);display:flex;padding-left:16px}
.nav a{font-family:"Oswald",sans-serif;font-size:15px;color:#fff;text-transform:uppercase;text-decoration:none;
  padding:0 18px;line-height:48px;letter-spacing:.5px}
.nav a.active{background:var(--green)}

/* condition strip */
.conditions{position:absolute;top:528px;left:0;width:1200px;height:64px;background:var(--blue);
  display:flex;justify-content:center;align-items:center;gap:34px}
.conditions span{font-family:"Oswald",sans-serif;font-size:15px;color:#fff;text-transform:uppercase;letter-spacing:.5px}

/* services */
.services-label{position:absolute;left:72px;top:760px;width:240px;height:220px;background:var(--blue);padding:40px 30px}
.services-label h2{font-family:"Oswald",sans-serif;font-weight:500;font-size:46px;color:#fff;line-height:1}
.services-label p{font-family:"Oswald",sans-serif;font-size:16px;color:#fff;letter-spacing:1px;margin-top:6px}
.service{position:absolute;width:260px;text-align:center}
.service svg{display:block;margin:0 auto 12px}
.service h3{font-family:"Oswald",sans-serif;font-weight:400;font-size:22px;color:var(--ink);margin-bottom:8px}
.service p{font-size:12px;line-height:18px;color:var(--muted)}

/* testimonial + faq */
.testimonial{position:absolute;left:0;top:1352px;width:420px;height:560px;
  background:linear-gradient(135deg,#4a4e54 0%,#2c2f34 60%,#1f2125 100%)}
.testimonial h2{position:absolute;left:48px;top:56px;font-family:"Oswald",sans-serif;font-weight:400;font-size:28px;color:#fff}
.quote-mark{position:absolute;left:48px;top:118px;font-family:"Lora",serif;font-size:64px;color:var(--blue);line-height:1}
.testimonial blockquote{position:absolute;left:96px;top:120px;width:290px;font-family:"Lora",serif;font-style:italic;
  font-size:21px;line-height:31px;color:#fff}
.author{position:absolute;left:96px;top:474px;display:flex;align-items:center;gap:12px}
.avatar{width:44px;height:44px;border-radius:50%;background:#8c7a6e}
.author b{display:block;font-size:13px;color:#fff;font-weight:600}
.author i{font-size:12px;color:#c8ccd1;font-style:normal}

.faq{position:absolute;left:420px;top:1352px;width:780px;height:560px;background:var(--blue);padding:52px 90px 0 80px}
.faq h2{font-family:"Oswald",sans-serif;font-weight:400;font-size:28px;color:#fff;margin-bottom:26px}
.faq-item{display:flex;align-items:center;gap:16px;height:52px;border-bottom:1px solid rgba(255,255,255,.25)}
.faq-item .toggle{width:30px;height:30px;background:var(--blue-dark);color:#fff;font-size:18px;text-align:center;line-height:30px}
.faq-item span{font-size:14px;font-weight:600;color:#fff}
.faq-answer{font-size:13px;line-height:21px;color:#e6f1fb;padding:18px 0 22px}
.view-all{display:inline-block;margin-top:26px;font-size:12px;font-weight:700;color:#fff;letter-spacing:.5px}

/* map */
.map{position:absolute;left:0;top:1912px;width:1200px;height:508px;background:var(--map)}

/* footer */
.footer{position:absolute;left:0;top:2420px;width:1200px;height:380px;background:var(--footer);padding:56px 72px 0}
.footer h4{font-family:"Oswald",sans-serif;font-weight:500;font-size:16px;color:#fff;letter-spacing:1px;margin-bottom:22px}
.col{position:absolute;top:56px}
.col p{font-size:13px;line-height:22px;color:#9aa0a8}
.posts li{list-style:none;font-size:12px;color:#9aa0a8;padding:10px 0 10px 18px;border-bottom:1px solid #2e3238;position:relative}
.posts li::before{content:"";position:absolute;left:0;top:15px;width:6px;height:6px;background:var(--blue)}
.tags{display:flex;flex-wrap:wrap;gap:8px;width:290px}
.tags span{font-size:10px;color:#c3c8cf;border:1px solid #3a3f46;padding:5px 12px;text-transform:uppercase}
.copyright{position:absolute;left:0;top:2800px;width:1200px;height:60px;background:var(--footer-deep);
  text-align:center;line-height:60px;font-size:12px;color:#7d838b;letter-spacing:.5px}
</style>
</head>
<body>

<section class="hero" role="img" aria-label="Photo of a man's bare back with a red glow over a sore shoulder"></section>
<header class="topbar">
  <div class="brand"><span class="brand-dot"></span><span class="brand-name">Verdell Chiropractic</span></div>
  <div class="social"><span></span><span></span><span></span><span></span></div>
  <nav class="nav">
    <a class="active">Home</a><a>About the Doc</a><a>Fibromyalgia</a><a>FAQs</a><a>Resources</a><a>Contact</a>
  </nav>
</header>

<div class="conditions">
  <span>Headaches</span><span>Shoulder Pain</span><span>Lower Back</span><span>Knee Pain</span><span>Fibromyalgia</span>
  <span>Neck Pain</span><span>Wrist Pain</span><span>Hip &amp; Leg Pain</span><span>Heel Pain</span><span>Disc Bulge</span>
</div>

<div class="services-label"><h2>SERVICES</h2><p>WE OFFER</p></div>

<div class="service" style="left:350px;top:760px">
  <svg width="50" height="50" viewBox="0 0 50 50" fill="none" stroke="#7a7f86" stroke-width="2"><rect x="20" y="4" width="10" height="8" rx="2"/><rect x="20" y="16" width="10" height="8" rx="2"/><rect x="20" y="28" width="10" height="8" rx="2"/><rect x="20" y="40" width="10" height="6" rx="2"/></svg>
  <h3>Chiropractic</h3>
  <p>As a doctor of chiropractic my advice is a hands-on approach to health care that includes patient examination, diagnosis and treatment.</p>
</div>
<div class="service" style="left:630px;top:760px">
  <svg width="50" height="50" viewBox="0 0 50 50" fill="none" stroke="#7a7f86" stroke-width="2"><line x1="10" y1="40" x2="40" y2="10"/><circle cx="40" cy="10" r="3"/><line x1="16" y1="46" x2="6" y2="36"/></svg>
  <h3>Acupuncture</h3>
  <p>The term acupuncture describes a family of procedures involving the stimulation of anatomical points on the body using a variety of techniques.</p>
</div>
<div class="service" style="left:900px;top:760px">
  <svg width="50" height="50" viewBox="0 0 50 50" fill="none" stroke="#7a7f86" stroke-width="2"><circle cx="30" cy="10" r="5"/><path d="M30 16 L22 30 L10 36 M22 30 L34 38 L40 46"/><line x1="4" y1="46" x2="46" y2="46"/></svg>
  <h3>Applied Kinesiology</h3>
  <p>Decades of experience in massage and myofascial therapy help patients recover faster from injuries and get relief from muscle tension.</p>
</div>

<div class="service" style="left:40px;top:1060px">
  <svg width="50" height="50" viewBox="0 0 50 50" fill="none" stroke="#7a7f86" stroke-width="2"><circle cx="25" cy="25" r="20"/><path d="M25 10 V40 M18 16 H32 M18 25 H32 M18 34 H32"/></svg>
  <h3>Spinal Decompression Therapy</h3>
  <p>Spinal decompression therapy is a non-surgical, gentle way to relieve back pain and neck pain caused by disc problems.</p>
</div>
<div class="service" style="left:330px;top:1060px">
  <svg width="50" height="50" viewBox="0 0 50 50" fill="none" stroke="#7a7f86" stroke-width="2"><circle cx="14" cy="20" r="5"/><path d="M4 34 H46 M10 34 C16 26 30 26 40 30"/><line x1="6" y1="40" x2="6" y2="46"/><line x1="44" y1="40" x2="44" y2="46"/></svg>
  <h3>Massage</h3>
  <p>Decades of experience in massage and myofascial therapy help patients recover faster from injuries and get relief from tension.</p>
</div>
<div class="service" style="left:620px;top:1060px">
  <svg width="50" height="50" viewBox="0 0 50 50" fill="none" stroke="#7a7f86" stroke-width="2"><rect x="14" y="14" width="22" height="32" rx="3"/><rect x="18" y="4" width="14" height="10"/><line x1="18" y1="28" x2="32" y2="28"/><line x1="25" y1="21" x2="25" y2="35"/></svg>
  <h3>Homeopathy</h3>
  <p>Homeopathy is a system of medical therapy that uses very small doses of a remedy to support the body's own healing process.</p>
</div>
<div class="service" style="left:900px;top:1060px">
  <svg width="50" height="50" viewBox="0 0 50 50" fill="none" stroke="#7a7f86" stroke-width="2"><rect x="6" y="8" width="38" height="28" rx="2"/><line x1="18" y1="44" x2="32" y2="44"/><line x1="25" y1="36" x2="25" y2="44"/><path d="M20 22 H30 M25 17 V27"/></svg>
  <h3>Other Services</h3>
  <p>As a doctor of chiropractic my advice is a hands-on approach to health care that includes patient examination.</p>
</div>

<section class="testimonial" role="img" aria-label="Dark photo of a smiling patient behind the testimonial">
  <h2>Testimonial</h2>
  <span class="quote-mark">&ldquo;</span>
  <blockquote>A wonderful serenity has taken possession of my entire soul, like these sweet mornings of spring which I enjoy with my whole heart. I am alone, and feel the charm of existence in this spot, which was created for the bliss of souls like mine.</blockquote>
  <div class="author"><span class="avatar"></span><div><b>Marla Quint</b><i>Patient</i></div></div>
</section>

<section class="faq">
  <h2>FAQ's</h2>
  <div class="faq-item"><span class="toggle">&minus;</span><span>We Provide Best Services</span></div>
  <p class="faq-answer">A wonderful serenity has taken possession of my entire soul, like these sweet mornings of spring which I enjoy with my whole heart. I am alone, and feel the charm of existence in this spot, which was created for the bliss of souls like mine. I am so happy, my dear friend, so absorbed in the exquisite sense of mere tranquil existence.</p>
  <div class="faq-item"><span class="toggle">+</span><span>Newest High Technology</span></div>
  <div class="faq-item"><span class="toggle">+</span><span>Qualified Great Doctors</span></div>
  <div class="faq-item"><span class="toggle">+</span><span>320 Machines</span></div>
  <span class="view-all">VIEW ALL FAQ &rsaquo;</span>
</section>

<section class="map" role="img" aria-label="Street map showing the clinic location"></section>

<footer class="footer">
  <div class="col" style="left:72px;width:290px">
    <h4>ABOUT US</h4>
    <p>A wonderful serenity has taken possession of my entire soul, like these sweet mornings of spring which I enjoy with my whole heart. I am alone, and feel the charm of existence in this spot, which was created for the bliss of souls.</p>
  </div>
  <div class="col" style="left:470px;width:300px">
    <h4>RECENT POSTS</h4>
    <ul class="posts">
      <li>Stretches that ease morning stiffness</li>
      <li>Five small steps toward a healthy spine</li>
      <li>Why posture matters at your desk</li>
      <li>Walking daily for better joint health</li>
    </ul>
  </div>
  <div class="col" style="left:840px">
    <h4>TAG CLOUD</h4>
    <div class="tags"><span>Wellness</span><span>Chiropractic</span><span>Massage</span><span>Spine</span><span>Health</span><span>Acupuncture</span><span>Pain</span><span>Posture</span><span>Homeopathy</span><span>Back</span></div>
  </div>
</footer>
<div class="copyright">COPYRIGHT 2016 VERDELL CHIROPRACTIC. ALL RIGHT RESERVED.</div>

</body>
</html>
```